Radiant Harvest Gathering 2021

I am looking to create a flyer for a one day prayer retreat our church is organizing. This flyer will be posted on social media, websites, mobile apps, and will also be printed so it can be mailed to people.

I am looking for something professional, with good use of our logo and band colors (logo colors).

I am counting on the designer's skill, creativity, art and knowledge of media communication to produce a flyer that will effectively and quickly convey the message we are trying to spread.

CONTENT OF THE FLYER:
Event title: Radiant Harvest Gathering
Date: Tuesday July 2nd, 2021
Time: 11:00AM - 7:00PM
Bellmore Hotel, 4817 Wexley Avenue, Portland, Maine 04109 (Room: Tamarind)
Event Key words to highlight what the event is about: Prayer, Fasting, Worship, Prophecy, Revival.
Key phrases:
A one day prayer retreat.
Jesus Chris is Lord

Contact info:
www.quvello.org
Phone: 207 555 0148
Email: contact@brookmeadow.org

```html
<!DOCTYPE html>
<html lang="en">
<head>
<meta charset="utf-8">
<title>Radiant Harvest Gathering 2021</title>
<link href="https://fonts.googleapis.com/css2?family=Roboto+Condensed:wght@700&family=Lato:wght@400;700&family=Oranienbaum&display=swap" rel="stylesheet">
<style>
  :root{
    --navy:#1c3a5e;
    --orange:#ec8a25;
    --white:#ffffff;
    --ink:#1d1d1d;
    --page:#e9e9e9;
    --sky-top:#f7f7f7;
    --sky-mid:#dfe1e4;
    --sun:#f2c27a;
    --ember:#8a2a1c;
    --ember-dark:#5a1a12;
  }
  *{box-sizing:border-box;margin:0;padding:0}
  html,body{width:1200px;height:1200px;overflow:hidden;background:var(--page)}
  .flyer{position:absolute;left:165px;top:40px;width:870px;height:1119px;background:var(--sky-top);overflow:hidden}
  .sky-photo{position:absolute;left:0;top:0;width:100%;height:940px;
    background:
      radial-gradient(ellipse 420px 220px at 260px 830px, rgba(245,190,110,.9), rgba(245,190,110,0) 70%),
      radial-gradient(ellipse 360px 300px at 720px 560px, rgba(214,190,170,.55), rgba(214,190,170,0) 70%),
      linear-gradient(180deg,var(--sky-top) 0%,#eef0f2 30%,var(--sky-mid) 55%,#e8d6b8 78%,var(--sun) 100%)}
  .bible-photo{position:absolute;left:0;top:940px;width:100%;height:156px;
    background:linear-gradient(180deg,#a0412a 0%,var(--ember) 40%,var(--ember-dark) 100%)}
  .brand{position:absolute;left:323px;top:49px;width:192px;height:119px;background:var(--navy);
    display:flex;align-items:center;justify-content:center;
    font-family:"Roboto Condensed",sans-serif;font-weight:700;font-size:38px;color:var(--white);letter-spacing:1px}
  .title{position:absolute;left:0;top:206px;width:100%;text-align:center;
    font-family:"Roboto Condensed",sans-serif;font-weight:700;font-size:56px;color:var(--navy);line-height:64px}
  .keywords{position:absolute;left:0;top:282px;width:100%;height:48px;background:var(--orange);
    display:flex;align-items:center;justify-content:center;
    font-family:"Lato",sans-serif;font-weight:700;font-size:23px;color:var(--white);letter-spacing:.5px}
  .tagline{position:absolute;left:0;top:366px;width:100%;text-align:center;
    font-family:"Oranienbaum",serif;font-size:64px;line-height:80px;color:var(--navy)}
  .date-box{position:absolute;left:252px;top:558px;width:329px;height:167px;border:1.5px solid var(--navy)}
  .date-line{position:absolute;left:24px;font-family:"Roboto Condensed",sans-serif;font-weight:700;font-size:50px;line-height:56px;color:var(--navy)}
  .day{top:18px}
  .month{top:80px}
  .month .num{background:var(--orange);color:var(--navy);padding:0 6px;margin-left:6px}
  .year{position:absolute;right:6px;top:83px;transform:translate(50%,-50%) rotate(90deg);transform-origin:center;
    font-family:"Roboto Condensed",sans-serif;font-weight:700;font-size:40px;color:var(--navy);right:34px}
  .time{position:absolute;left:0;top:736px;width:100%;text-align:center;
    font-family:"Lato",sans-serif;font-weight:700;font-size:28px;color:var(--navy)}
  .pin{position:absolute;left:422px;top:790px;width:26px;height:30px}
  .venue{position:absolute;left:0;top:828px;width:100%;text-align:center;
    font-family:"Lato",sans-serif;font-weight:700;font-size:22px;color:var(--ink)}
  .room{position:absolute;left:0;top:857px;width:100%;text-align:center;
    font-family:"Lato",sans-serif;font-weight:700;font-size:21px;color:var(--navy)}
  .rule{position:absolute;left:0;width:100%;height:2px;background:var(--navy)}
  .rule.one{top:934px}
  .rule.two{top:940px;height:1px;background:#c9b9a6}
  .contact-label{position:absolute;left:315px;top:919px;width:191px;height:42px;background:var(--navy);
    display:flex;align-items:center;justify-content:center;
    font-family:"Lato",sans-serif;font-weight:700;font-size:28px;color:var(--white)}
  .phone{position:absolute;left:0;top:981px;width:100%;display:flex;align-items:center;justify-content:center;gap:12px;
    font-family:"Lato",sans-serif;font-weight:700;font-size:37px;color:var(--white)}
  .phone svg{width:40px;height:40px}
  .web-line{position:absolute;left:0;top:1036px;width:100%;text-align:center;
    font-family:"Lato",sans-serif;font-size:22px;color:var(--white)}
  .web-line .sep{margin:0 10px}
  .footer-bar{position:absolute;left:0;top:1096px;width:100%;height:23px;background:var(--navy)}
</style>
</head>
<body>
  <main class="flyer">
    <div class="sky-photo" role="img" aria-label="Photo of a cross against a golden sunrise sky with birds and hands folded in prayer"></div>
    <div class="bible-photo" role="img" aria-label="Photo of an open Holy Bible in warm red light"></div>

    <div class="brand">QUVELLO</div>

    <h1 class="title">RADIANT HARVEST GATHERING</h1>
    <div class="keywords">PRAYER&nbsp;|&nbsp;FASTING&nbsp;|&nbsp;WORSHIP&nbsp;|&nbsp;PROPHECY&nbsp;|&nbsp;REVIVAL.</div>

    <p class="tagline">A one day prayer retreat.<br>Jesus Chris is Lord</p>

    <div class="date-box">
      <div class="date-line day">TUESDAY</div>
      <div class="date-line month">JULY<span class="num">2ND</span></div>
      <div class="year">2021</div>
    </div>

    <p class="time">11:00AM - 7:00PM</p>

    <svg class="pin" viewBox="0 0 26 30" aria-hidden="true">
      <path d="M13 1C6.9 1 2 5.8 2 11.8 2 19.5 13 29 13 29s11-9.5 11-17.2C24 5.8 19.1 1 13 1z" fill="none" stroke="#1c3a5e" stroke-width="3"/>
      <circle cx="13" cy="11.5" r="4" fill="#1c3a5e"/>
    </svg>
    <p class="venue">Bellmore Hotel, 4817 Wexley Avenue, Portland, Maine 04109</p>
    <p class="room">(Room : Tamarind)</p>

    <div class="rule one"></div>
    <div class="rule two"></div>
    <div class="contact-label">Contact Us</div>

    <p class="phone">
      <svg viewBox="0 0 40 40" aria-hidden="true">
        <circle cx="20" cy="20" r="17.5" fill="none" stroke="#ffffff" stroke-width="2.5"/>
        <path d="M14.5 11.5l3 .3 1.6 4.4-2 1.6c1 2.3 2.8 4.2 5.1 5.3l1.7-2 4.3 1.7.2 3c-.1 1.2-1.2 2.2-2.5 2.1C17.8 27.6 12.3 22 12.2 14c0-1.3 1-2.4 2.3-2.5z" fill="#ffffff"/>
      </svg>
      207 555 0148
    </p>
    <p class="web-line">contact@brookmeadow.org<span class="sep">|</span>www.quvello.org</p>

    <div class="footer-bar"></div>
  </main>
</body>
</html>
```